Railroad Association needs One-Page Infographic

Please see attachment for text and graphic. email with questions please. This piece will be handed out to legislators and state officials.

Target Market(s)

state legislature. state officials

Font styles to use
Serif

Colors
ec1f27

Requirements
Must have
• The graphic needs to be done right. Please email me with any questions.

```html
<!DOCTYPE html>
<html lang="en">
<head>
<meta charset="utf-8">
<title>Keys to a Safe and Thorough Process</title>
<link href="https://fonts.googleapis.com/css2?family=Open+Sans:wght@600;700&family=Cormorant+SC:wght@700&display=swap" rel="stylesheet">
<style>
  :root {
    --brand-red: #ec1f27;
    --header-dark: #3b3b3c;
    --step-text: #58595b;
    --frame-grey: #c9cacb;
    --paper: #ffffff;
  }
  html, body {
    margin: 0;
    padding: 0;
    overflow: hidden;
    background: var(--paper);
  }
  .sheet {
    position: relative;
    width: 851px;
    height: 1200px;
    overflow: hidden;
    background: var(--paper);
  }
  .header {
    position: absolute;
    left: 0; top: 0;
    width: 100%;
    height: 282px;
    background: var(--header-dark);
  }
  .header-rule {
    position: absolute;
    left: 0; top: 282px;
    width: 100%;
    height: 11px;
    background: var(--brand-red);
  }
  .title {
    position: absolute;
    left: 40px; top: 46px;
    margin: 0;
    font-family: "Open Sans", sans-serif;
    font-weight: 600;
    font-size: 56px;
    line-height: 64px;
    letter-spacing: 2px;
    color: #fff;
    text-transform: uppercase;
  }
  .title .accent { color: var(--brand-red); font-weight: 700; }
  .scene-backdrop {
    position: absolute;
    left: 0; top: 640px;
    width: 100%;
    height: 538px;
    background: linear-gradient(180deg, rgba(255,255,255,1) 0%, rgba(226,228,226,0.8) 35%, rgba(200,204,196,0.85) 70%, rgba(214,216,210,0.9) 100%);
  }
  .steps {
    position: absolute;
    left: 37px; top: 342px;
    margin: 0; padding: 0;
    list-style: none;
  }
  .step {
    display: flex;
    align-items: center;
    height: 108px;
    margin-bottom: 14px;
  }
  .step-box {
    width: 108px; height: 108px;
    box-sizing: border-box;
    border: 7px solid var(--frame-grey);
    background: var(--brand-red);
    display: flex;
    align-items: center;
    justify-content: center;
  }
  .step-label {
    margin-left: 40px;
    font-family: "Cormorant SC", serif;
    font-weight: 700;
    font-size: 62px;
    letter-spacing: 2px;
    color: var(--step-text);
  }
  .org-name {
    position: absolute;
    left: 620px; top: 1068px;
    width: 200px;
    display: flex;
    align-items: center;
    gap: 10px;
    font-family: "Cormorant SC", serif;
    font-weight: 700;
    font-size: 22px;
    line-height: 24px;
    color: var(--header-dark);
  }
  .org-name .org-square {
    flex: none;
    width: 14px; height: 14px;
    background: var(--header-dark);
  }
  .footer-bar {
    position: absolute;
    left: 0; bottom: 0;
    width: 100%;
    height: 22px;
    background: var(--brand-red);
  }
</style>
</head>
<body>
<div class="sheet">
  <div class="header">
    <h1 class="title">Keys to a <span class="accent">Safe</span><br>and Thorough<br>Process</h1>
  </div>
  <div class="header-rule"></div>

  <div class="scene-backdrop" role="img" aria-label="Faded photograph of a railroad crossing with signal gates in open countryside"></div>

  <ul class="steps">
    <li class="step">
      <span class="step-box"><svg width="52" height="52" viewBox="0 0 52 52" aria-hidden="true"><rect x="4" y="10" width="36" height="36" fill="none" stroke="#fff" stroke-width="4"/><path d="M13 27 L22 36 L46 8" fill="none" stroke="#fff" stroke-width="6" stroke-linecap="square"/></svg></span>
      <span class="step-label">Plan</span>
    </li>
    <li class="step">
      <span class="step-box"><svg width="52" height="52" viewBox="0 0 52 52" aria-hidden="true"><rect x="4" y="10" width="36" height="36" fill="none" stroke="#fff" stroke-width="4"/><path d="M13 27 L22 36 L46 8" fill="none" stroke="#fff" stroke-width="6" stroke-linecap="square"/></svg></span>
      <span class="step-label">Review</span>
    </li>
    <li class="step">
      <span class="step-box"><svg width="52" height="52" viewBox="0 0 52 52" aria-hidden="true"><rect x="4" y="10" width="36" height="36" fill="none" stroke="#fff" stroke-width="4"/><path d="M13 27 L22 36 L46 8" fill="none" stroke="#fff" stroke-width="6" stroke-linecap="square"/></svg></span>
      <span class="step-label">Communicate</span>
    </li>
    <li class="step">
      <span class="step-box"><svg width="52" height="52" viewBox="0 0 52 52" aria-hidden="true"><rect x="4" y="10" width="36" height="36" fill="none" stroke="#fff" stroke-width="4"/><path d="M13 27 L22 36 L46 8" fill="none" stroke="#fff" stroke-width="6" stroke-linecap="square"/></svg></span>
      <span class="step-label">Agree</span>
    </li>
    <li class="step">
      <span class="step-box"><svg width="52" height="52" viewBox="0 0 52 52" aria-hidden="true"><rect x="4" y="10" width="36" height="36" fill="none" stroke="#fff" stroke-width="4"/><path d="M13 27 L22 36 L46 8" fill="none" stroke="#fff" stroke-width="6" stroke-linecap="square"/></svg></span>
      <span class="step-label">Install</span>
    </li>
  </ul>

  <div class="org-name">
    <span class="org-square"></span>
    <span>Lakeshore Rail Council</span>
  </div>

  <div class="footer-bar"></div>
</div>
</body>
</html>
```